Website for a new investor-focused estate agency portal

Require a website for a new investor-focused estate agency portal, this will interface with our exisitng API for data posting and retrieval. We have a logo for the business, but will happily change the colour palette to suit the design.
Requirements:
1) Landing page to describe the business
- Feature line showing the latest properties in our listings
- Announcement section (e.g. mobile app coming soon)
- Text area - what we do for Investors
- Text area - what we do for Agents and sourcers
- Text area - what we do for Home buyers
- Small Q&A
- Subscription pricing description and sign up
2) Content page (product updates page)
A timeline to list list releases, new features and other improvements to the service, website and app, shown in most recent date order.
3) A property search/result page including search form
4) A single property detail page, including
- carousel for images and video
- map
- text content
5) A data entry page to enter property data into the system. This page will contain a sidebar menu, property name, address, description, and about 10 other fields (detail to be provided). The attached screen dump files are snapshot of the wireframe form used by the development team for the property entry page.
Target Market(s)
Property investors / Real estate buyer's including personal home buyers.
Number of Pages Required
5+ page
Colors
Designer to choose colors to be used in the design.
Requirements
Must have
- Clean, crisp design and presentaion.
Nice to have
- The Search/result page (3) and the detail page (4) may have 2-3 elements for paid advertising but should also look good without those elements.
Should not have
- Must not be too busy with distracting elements

```html
<!DOCTYPE html>
<html lang="en">
<head>
<meta charset="utf-8">
<title>Keystone Estates — Investor Property Portal</title>
<link rel="stylesheet" href="https://fonts.googleapis.com/css2?family=Roboto:wght@400;500;700&display=swap">
<style>
  :root{
    --blue:#0a78ff;
    --navy:#2c2a6b;
    --navy-soft:#3a3878;
    --ink:#1f1d4d;
    --text:#4a4a5a;
    --grey-btn:#d4d4d8;
    --faq-bg:#eef0f1;
    --white:#ffffff;
    --dark:#141418;
  }
  *{box-sizing:border-box;margin:0;padding:0}
  html,body{width:1200px;height:2917px;overflow:hidden}
  body{font-family:"Roboto",Arial,sans-serif;color:var(--text);background:var(--white);position:relative}
  .section{position:absolute;left:0;width:1200px;overflow:hidden}
  .photo{position:absolute}

  /* Header + hero */
  .hero{top:0;height:480px}
  .hero .photo{inset:0;background:
      linear-gradient(90deg,rgba(200,200,205,.55) 0%,rgba(255,255,255,0) 12%,rgba(255,255,255,0) 88%,rgba(200,200,205,.55) 100%),
      linear-gradient(180deg,#0f6ff5 0%,#5f9cf0 16%,#cfd9e6 34%,#ecedef 55%,#e6e2dc 78%,#d8cfc3 100%)}
  .brand{position:absolute;left:249px;top:28px;font-size:17px;font-weight:700;color:var(--white);display:flex;align-items:center;gap:8px;white-space:nowrap}
  .brand-dot{width:12px;height:12px;background:var(--white);flex:none}
  .nav{position:absolute;top:36px;left:685px}
  .nav a{position:absolute;color:var(--white);font-size:11px;font-weight:500;text-decoration:none;white-space:nowrap}
  .nav a.active::after{content:"";position:absolute;left:0;right:0;top:20px;height:2px;background:var(--white)}
  .hero-title{position:absolute;top:213px;left:0;width:1200px;text-align:center;font-size:26px;font-weight:500;color:var(--ink)}
  .search{position:absolute;top:257px;left:393px;height:29px;display:flex}
  .search .field{height:29px;background:var(--white);font-size:10px;color:#555;display:flex;align-items:center;padding-left:12px;border:1px solid #ddd}
  .search .city{width:97px;justify-content:space-between;padding-right:10px}
  .search .location{width:220px;margin-left:4px}
  .search .find{width:81px;margin-left:6px;background:var(--navy);color:var(--white);font-size:10px;font-weight:500;display:flex;align-items:center;justify-content:center}
  .search-links{position:absolute;top:291px;left:405px;font-size:8px;color:#333;white-space:nowrap}

  /* Audience bands */
  .band .heading{position:absolute;font-size:22px;font-weight:700;color:var(--white);white-space:nowrap}
  .band-investors{top:480px;height:296px;background:var(--navy)}
  .band-investors .photo{left:545px;top:0;width:655px;height:296px;background:
      linear-gradient(90deg,var(--navy) 0%,rgba(44,42,107,0) 35%),
      linear-gradient(180deg,#6d6aa0 0%,#8d7f80 40%,#a48f80 70%,#6a5f70 100%)}
  .products{top:776px;height:480px}
  .band-agents{top:1256px;height:290px;background:var(--blue)}
  .band-agents .photo{left:230px;top:0;width:334px;height:290px;background:
      linear-gradient(90deg,var(--blue) 0%,rgba(10,120,255,0) 18%,rgba(10,120,255,0) 82%,var(--blue) 100%),
      linear-gradient(180deg,#3e8ff8 0%,#9fc0ea 40%,#e8ecf2 75%,#f4f5f7 100%)}
  .faq{top:1546px;height:485px;background:var(--faq-bg)}
  .band-buyers{top:2031px;height:291px;background:var(--navy)}
  .band-buyers .photo{left:574px;top:0;width:360px;height:291px;background:
      linear-gradient(90deg,var(--navy) 0%,rgba(44,42,107,0) 20%,rgba(44,42,107,0) 80%,var(--navy) 100%),
      linear-gradient(180deg,#3e3c7c 0%,#6c5e84 40%,#8a6d78 65%,#4d5c8e 100%)}

  /* Product */
  .products .title{position:absolute;top:38px;left:0;width:1200px;text-align:center;font-size:22px;font-weight:700;color:var(--ink)}
  .arrow{position:absolute;top:35px}
  .card{position:absolute;top:107px;width:218px}
  .card .photo{position:relative;width:218px;height:207px;background:linear-gradient(180deg,#b8d3ee 0%,#c9c7c0 45%,#8a8f84 65%,#5e8a3f 100%)}
  .card .tag{position:absolute;top:192px;left:50px;width:118px;height:27px;background:var(--blue);color:var(--white);font-size:9px;font-weight:500;display:flex;align-items:center;justify-content:center}
  .card .name{margin-top:24px;text-align:center;font-size:14px;font-weight:500;color:var(--ink)}
  .card .specs{margin-top:6px;display:flex;justify-content:center;gap:20px;font-size:8px;color:#333}
  .card .actions{margin-top:12px;display:flex;justify-content:space-between}
  .card .price,.card .pid{width:104px;height:28px;font-size:8.5px;display:flex;align-items:center;justify-content:center}
  .card .price{background:var(--grey-btn);color:#555}
  .card .pid{background:var(--navy);color:var(--white)}

  /* FAQ */
  .faq .title{position:absolute;top:40px;left:0;width:1200px;text-align:center;font-size:22px;font-weight:700;color:var(--ink)}
  .faq-item{position:absolute;width:325px;height:30px;background:var(--white);box-shadow:0 1px 2px rgba(0,0,0,.08);display:flex;align-items:center;justify-content:space-between;padding:0 12px;font-size:9px;font-weight:500;color:var(--ink);white-space:nowrap}
  .faq-item.open{background:var(--navy);color:var(--white)}
  .faq-item .plus{font-size:15px;font-weight:400}
  .faq-answer{position:absolute;left:271px;top:145px;width:305px;font-size:9px;line-height:1.75;color:#666}
  .read-more{position:absolute;top:407px;left:560px;width:80px;height:29px;background:var(--navy);color:var(--white);font-size:9px;font-weight:500;display:flex;align-items:center;justify-content:center}

  /* Newsletter */
  .newsletter{top:2322px;height:267px;background:var(--dark)}
  .newsletter .photo{left:0;top:0;width:500px;height:267px;background:
      linear-gradient(90deg,rgba(20,20,24,0) 70%,var(--dark) 100%),
      linear-gradient(115deg,#5a6a8c 0%,#a39384 22%,#e6e3de 45%,#f2efe9 60%,#bfb8ae 100%)}
  .newsletter h2{position:absolute;left:615px;top:61px;font-size:24px;font-weight:700;color:var(--white)}
  .newsletter p{position:absolute;left:615px;top:100px;width:340px;font-size:9.5px;line-height:1.75;color:#e6e6e6}
  .subscribe{position:absolute;left:615px;top:168px;display:flex}
  .subscribe .email{width:222px;height:29px;background:var(--white);font-size:9px;color:#888;display:flex;align-items:center;padding-left:10px}
  .subscribe .btn{width:115px;height:29px;background:var(--blue);color:var(--white);font-size:9px;font-weight:500;display:flex;align-items:center;justify-content:center}

  /* Footer */
  .footer{top:2589px;height:328px;background:var(--white)}
  .footer .brand{color:var(--navy);top:68px;left:249px;width:95px;font-size:15px;line-height:1.25;white-space:normal;align-items:flex-start}
  .footer .brand .brand-dot{background:var(--navy);margin-top:3px}
  .footer h3{position:absolute;top:64px;font-size:13px;font-weight:700;color:var(--ink)}
  .footer .about{position:absolute;left:358px;top:105px;width:265px;font-size:9.5px;line-height:1.7;color:#666}
  .contact-row{position:absolute;display:flex;gap:8px;font-size:9.5px;color:#666;line-height:1.7}
  .contact-row svg{margin-top:2px;flex:none}
  .contact-row strong{color:var(--ink);font-weight:500;display:block}
  .footer .rule{position:absolute;left:249px;top:227px;width:702px;height:1px;background:#e3e3e6}
  .footer .copy{position:absolute;left:249px;top:251px;font-size:9px;color:#666}
</style>
</head>
<body>

<header class="section hero">
  <div class="photo" role="img" aria-label="Bright living room interior with sofa, coffee table and plants"></div>
  <div class="brand"><span class="brand-dot"></span>Keystone Estates</div>
  <nav class="nav">
    <a class="active" href="#" style="left:0">Home</a>
    <a href="#" style="left:50px">About Us</a>
    <a href="#" style="left:115px">Product</a>
    <a href="#" style="left:175px">FAQ</a>
    <a href="#" style="left:215px">Contact Us</a>
  </nav>
  <h1 class="hero-title">Latest Properties in Our Listings</h1>
  <form class="search">
    <div class="field city">City
      <svg width="8" height="5" viewBox="0 0 8 5"><path d="M0 0l4 5 4-5z" fill="#555"/></svg>
    </div>
    <div class="field location">Location</div>
    <div class="find">Find</div>
  </form>
  <div class="search-links">▾ More Options &nbsp;|&nbsp; Change Currency &nbsp;|&nbsp; Change Area Unit &nbsp;|&nbsp; Reset Search</div>
</header>

<section class="section band band-investors">
  <div class="photo" role="img" aria-label="Modern two-storey house exterior"></div>
  <h2 class="heading" style="left:249px;top:132px">What We Do For Investors</h2>
</section>

<section class="section products">
  <h2 class="title">Product</h2>
  <svg class="arrow" style="left:249px" width="33" height="33" viewBox="0 0 33 33"><circle cx="16.5" cy="16.5" r="15.5" fill="none" stroke="#2c2a6b" stroke-width="2"/><path d="M19 10l-6 6.5 6 6.5" fill="none" stroke="#2c2a6b" stroke-width="2"/></svg>
  <svg class="arrow" style="left:918px" width="33" height="33" viewBox="0 0 33 33"><circle cx="16.5" cy="16.5" r="15.5" fill="none" stroke="#2c2a6b" stroke-width="1.5"/><path d="M14 10l6 6.5-6 6.5" fill="none" stroke="#2c2a6b" stroke-width="1.5"/></svg>

  <article class="card" style="left:249px">
    <div class="photo" role="img" aria-label="Family home with grey roof and front lawn"></div>
    <div class="tag">Single Family Home</div>
    <div class="name">Maple Grove Subdivision</div>
    <div class="specs"><span>3 Bed's</span><span>1 Bath</span><span>2225sq ft</span></div>
    <div class="actions"><span class="price">£39420 / Day</span><span class="pid">Property Id: 4287</span></div>
  </article>
  <article class="card" style="left:491px">
    <div class="photo" role="img" aria-label="Family home at dusk with lit windows and garden" style="background:linear-gradient(180deg,#cfd9e3 0%,#9a9488 35%,#5f6a55 65%,#3f6a2e 100%)"></div>
    <div class="tag">Single Family Home</div>
    <div class="name">Maple Grove Subdivision</div>
    <div class="specs"><span>3 Bed's</span><span>1 Bath</span><span>2225sq ft</span></div>
    <div class="actions"><span class="price">£39420 / Day</span><span class="pid">Property Id: 4287</span></div>
  </article>
  <article class="card" style="left:733px">
    <div class="photo" role="img" aria-label="Timber house among trees with garden seating" style="background:linear-gradient(180deg,#a9bb86 0%,#8a6a4c 40%,#6e5038 65%,#5f7d3a 100%)"></div>
    <div class="tag">Single Family Home</div>
    <div class="name">Maple Grove Subdivision</div>
    <div class="specs"><span>3 Bed's</span><span>1 Bath</span><span>2225sq ft</span></div>
    <div class="actions"><span class="price">£39420 / Day</span><span class="pid">Property Id: 4287</span></div>
  </article>
</section>

<section class="section band band-agents">
  <div class="photo" role="img" aria-label="Smiling agent giving a thumbs up and holding a small model house"></div>
  <h2 class="heading" style="left:543px;top:131px">What We Do For Agents and Sourcers</h2>
</section>

<section class="section faq">
  <h2 class="title">FAQs</h2>
  <div class="faq-item open" style="left:259px;top:104px"><span>Lorem Ipsum is simply dummy text of the printing.</span><span class="plus">+</span></div>
  <p class="faq-answer">Lorem Ipsum has been the industry's standard dummy text ever since the 1500s, when an unknown printer took a galley of type and scrambled it to make a type specimen book.</p>
  <div class="faq-item" style="left:259px;top:209px"><span>Lorem Ipsum is simply dummy text of the printing.</span><span class="plus">+</span></div>
  <div class="faq-item" style="left:259px;top:261px"><span>Lorem Ipsum is simply dummy text of the printing.</span><span class="plus">+</span></div>
  <div class="faq-item" style="left:259px;top:314px"><span>Lorem Ipsum is simply dummy text of the printing.</span><span class="plus">+</span></div>
  <div class="faq-item" style="left:616px;top:104px"><span>Lorem Ipsum is simply dummy text of the printing.</span><span class="plus">+</span></div>
  <div class="faq-item" style="left:616px;top:156px"><span>Lorem Ipsum is simply dummy text of the printing.</span><span class="plus">+</span></div>
  <div class="faq-item" style="left:616px;top:209px"><span>Lorem Ipsum is simply dummy text of the printing.</span><span class="plus">+</span></div>
  <div class="faq-item" style="left:616px;top:261px"><span>Lorem Ipsum is simply dummy text of the printing.</span><span class="plus">+</span></div>
  <div class="read-more">Read More</div>
</section>

<section class="section band band-buyers">
  <div class="photo" role="img" aria-label="Happy couple sitting together on a sofa"></div>
  <h2 class="heading" style="left:249px;top:129px">What We Do For Home Buyers</h2>
</section>

<section class="section newsletter">
  <div class="photo" role="img" aria-label="Person reading a newspaper beside a cup of coffee"></div>
  <h2>Newsletter</h2>
  <p>Lorem Ipsum has been the industry's standard dummy text ever since the when an unknown printer took a galley of type and scrambled it to make a type specimen book.</p>
  <form class="subscribe"><div class="email">Email Enter...</div><div class="btn">Subscription</div></form>
</section>

<footer class="section footer">
  <div class="brand"><span class="brand-dot"></span><span>Keystone Estates</span></div>
  <h3 style="left:358px">About Us</h3>
  <p class="about">Lorem Ipsum has been the industry's standard dummy text ever since the when an unknown printer took a galley of type and scrambled it to make a type specimen book. Lorem Ipsum has been the industry's standard dummy text ever since.</p>
  <h3 style="left:667px">Contact</h3>
  <div class="contact-row" style="left:667px;top:103px">
    <svg width="12" height="12" viewBox="0 0 24 24"><path d="M6.6 10.8a15.1 15.1 0 006.6 6.6l2.2-2.2a1 1 0 011-.25 11.4 11.4 0 003.6.57 1 1 0 011 1V20a1 1 0 01-1 1A17 17 0 013 4a1 1 0 011-1h3.5a1 1 0 011 1c0 1.25.2 2.45.57 3.57a1 1 0 01-.25 1z" fill="#2c2a6b"/></svg>
    <div><strong>Phone:</strong>(000) 000 0000</div>
  </div>
  <div class="contact-row" style="left:667px;top:153px">
    <svg width="12" height="12" viewBox="0 0 24 24"><rect x="2" y="5" width="20" height="14" rx="1" fill="#2c2a6b"/><path d="M2 6l10 7 10-7" fill="none" stroke="#fff" stroke-width="1.6"/></svg>
    <div><strong>Address:</strong>ABC Street City 12345</div>
  </div>
  <h3 style="left:840px">Open Hours</h3>
  <div class="contact-row" style="left:840px;top:103px">
    <svg width="12" height="12" viewBox="0 0 24 24"><circle cx="12" cy="12" r="10" fill="none" stroke="#2c2a6b" stroke-width="2.4"/><path d="M12 6v6l4 2" fill="none" stroke="#2c2a6b" stroke-width="2.4"/></svg>
    <div><strong>Monday - Friday:</strong>9:00AM - 5:00PM</div>
  </div>
  <div class="rule"></div>
  <p class="copy">Copyright 2019 Estate Agency. All Rights Reserved.</p>
</footer>

</body>
</html>
```